Website for an AdOps/Media Agency

We need a logo for an ad operations firm. We help websites to maximize their advertising revenues by optimizing their ad networks, configurations, technologies, etc. The name is Zornival, or ZorNival, to communicate that we take them to the top of their revenue potential. We want to also communicate, trust us to handle your adops, we take care of the hassle (it's an industry in continual technological innovation -- hard to stay on top of, and heavily manual, reporting, etc) and make sure our clients maximize ad revenues. For more info on site ideas/desires: https://files.brelmora.com/doc/7QxTbn2Lw9Rk4Vz8Hc3Md6Fp1Ys5Ga0Je/view?usp=sharing
Updates

Project Deadline Extended Reason: Apologies, I got caught up in other things. This is now priority, and will be guaranteed. I will also include an extra coding fee for a WP site and increase the budget. Thanks for your understanding! Added Thursday, July 7, 2016

Target Market(s)

Ad Operations/Media Consultancy

Industry/Entity Type

Ad Agency

Number of Pages Required

1 page

Font styles to use
Sans Serif

Requirements
Must have
• I like clean and simple, nice images, scrolling down.
Nice to have
• I like clean, fresh white running through the site. Note, I listed us as an ad agency, but only because there was no adops. We work with ad agencies, but we are more agents for publishers.
Should not have
• To much clutter.

```html
<!DOCTYPE html>
<html lang="en">
<head>
<meta charset="utf-8">
<title>Zornival — Ad Operations</title>
<link rel="stylesheet" href="https://fonts.googleapis.com/css2?family=Montserrat:wght@400;600;700&family=Open+Sans:wght@400;600;700&family=Questrial&display=swap">
<style>
:root{
  --green:#4cae4c;
  --green-dark:#3d8f3d;
  --ink:#1d1d1d;
  --muted:#6b6b6b;
  --white:#ffffff;
  --footer:#333333;
  --footer-deep:#111111;
  --field:#0b0b0b;
}
*{box-sizing:border-box;margin:0;padding:0}
html,body{width:1200px;height:3249px;overflow:hidden;background:var(--white)}
body{font-family:"Open Sans",Arial,sans-serif;color:var(--ink);position:relative}

/* Header */
.site-header{position:absolute;top:0;left:0;width:1200px;height:173px;display:flex;align-items:center;justify-content:space-between;padding:0 40px 0 54px}
.brand{display:flex;align-items:center;gap:22px}
.brand-square{width:66px;height:66px;border:3px solid var(--ink);border-radius:6px}
.brand-name{font-family:"Questrial",Arial,sans-serif;font-weight:400;font-size:54px;color:var(--green);letter-spacing:-1px}
.main-nav{display:flex;align-items:center;margin-top:6px}
.main-nav a{font-family:"Open Sans",Arial,sans-serif;font-weight:600;font-size:15.5px;color:var(--ink);text-decoration:none;margin-right:30px;padding:10px 0;position:relative}
.main-nav a.is-active::after{content:"";position:absolute;left:0;right:0;bottom:-2px;height:4px;background:var(--green)}
.main-nav .btn-consult{background:var(--green);color:var(--white);padding:11px 14px;border-radius:4px;margin-right:12px}

/* Hero */
.hero{position:absolute;top:173px;left:0;width:1200px;height:553px;background:linear-gradient(180deg,#5d7fa5 0%,#a9bfd6 30%,#e7eef5 60%,#f5f8fb 100%)}
.hero-visual{position:absolute;inset:0;background:radial-gradient(ellipse at 72% 55%,rgba(60,80,110,.35),rgba(0,0,0,0) 45%),linear-gradient(160deg,rgba(255,255,255,0) 40%,rgba(255,255,255,.55) 80%)}
.hero-copy{position:absolute;left:93px;top:180px;width:520px}
.hero-title{font-family:"Questrial",Arial,sans-serif;font-weight:400;font-size:46px;color:#111;margin-bottom:14px}
.hero-text{font-family:"Questrial",Arial,sans-serif;font-size:20px;line-height:27px;color:#222}
.btn-learn{display:inline-block;margin-top:20px;background:var(--green);color:var(--white);font-family:"Questrial",Arial,sans-serif;font-size:20px;width:180px;height:37px;line-height:37px;text-align:center;border-radius:3px;text-decoration:none}
.hero-dots{position:absolute;left:572px;top:530px;display:flex;gap:6px}
.hero-dots span{width:9px;height:9px;border-radius:50%;background:#222}
.hero-dots span.is-active{background:#fff}

/* Intro band */
.intro{position:absolute;top:726px;left:0;width:1200px;height:173px;background:var(--green);color:var(--white);text-align:center;padding-top:36px}
.intro-title{font-family:"Montserrat",Arial,sans-serif;font-weight:400;font-size:29px;margin-bottom:16px}
.intro-title strong{font-weight:700}
.intro-text{font-size:16px;line-height:24px;width:940px;margin:0 auto}

/* Services */
.services{position:absolute;top:899px;left:0;width:1200px;padding-top:45px}
.service{height:140px;display:flex;align-items:center}
.service--left{padding-left:104px}
.service--right{flex-direction:row-reverse;padding-right:104px}
.service-icon{width:104px;height:104px;border:3px solid var(--ink);border-radius:9px;flex:none;display:flex;align-items:center;justify-content:center}
.service-icon svg{width:62px;height:62px;fill:none;stroke:var(--green);stroke-width:3;stroke-linecap:round;stroke-linejoin:round}
.service-chevron{font-family:"Montserrat",Arial,sans-serif;font-size:18px;color:var(--ink);width:40px;text-align:center;flex:none}
.service-body{max-width:845px}
.service--right .service-body{max-width:860px}
.service-title{font-family:"Montserrat",Arial,sans-serif;font-weight:700;font-size:18px;color:#000;margin-bottom:4px}
.service-text{font-size:13.5px;line-height:20px;color:var(--muted)}

/* Subscribe */
.subscribe{position:absolute;top:2809px;left:0;width:1200px;height:87px;background:var(--green);display:flex;align-items:center;padding-left:121px}
.subscribe-title{font-family:"Questrial",Arial,sans-serif;font-weight:400;font-size:27px;color:var(--white);width:375px}
.subscribe-field{width:230px;height:43px;background:var(--green-dark);color:var(--white);font-size:13px;padding:0 14px;line-height:43px;margin-right:10px}
.subscribe-btn{width:104px;height:43px;background:var(--footer-deep);color:var(--white);font-family:"Montserrat",Arial,sans-serif;font-weight:700;font-size:12px;line-height:43px;text-align:center;margin-left:3px}

/* Footer */
.site-footer{position:absolute;top:2896px;left:0;width:1200px;height:305px;background:var(--footer);color:var(--white)}
.footer-col{position:absolute;top:52px}
.footer-heading{font-family:"Montserrat",Arial,sans-serif;font-weight:700;font-size:14px;text-transform:uppercase;padding-bottom:12px;border-bottom:1px solid #555;width:168px;margin-bottom:20px}
.quick-links{left:71px}
.quick-links li{list-style:none;font-size:13px;line-height:26px;text-transform:uppercase}
.contact{left:295px}
.contact-item{display:flex;gap:14px;font-size:13px;line-height:19px;margin-bottom:18px}
.contact-item svg{width:16px;height:16px;fill:var(--white);flex:none;margin-top:2px}
.message{left:548px}
.message .footer-heading{border-bottom:none;width:auto}
.message-field{width:238px;height:29px;background:var(--field);font-size:11px;font-weight:700;padding:6px 10px;margin-bottom:7px}
.message-field--area{height:58px}
.message-btn{width:104px;height:26px;background:var(--field);font-family:"Montserrat",Arial,sans-serif;font-weight:700;font-size:12px;line-height:26px;text-align:center;margin-top:4px}
.footer-brand{position:absolute;left:866px;top:120px;display:flex;align-items:center;gap:20px}
.footer-brand .brand-square{width:56px;height:56px;border-color:var(--white)}
.footer-brand .brand-name{color:var(--white);font-size:44px}

.copyright{position:absolute;top:3201px;left:0;width:1200px;height:48px;background:var(--footer-deep);color:var(--white);display:flex;align-items:center;justify-content:space-between;padding:0 36px 0 48px;font-family:"Montserrat",Arial,sans-serif;font-weight:700;font-size:11px}
.social{display:flex;gap:6px}
.social span{width:20px;height:20px;border-radius:50%;background:var(--white)}
</style>
</head>
<body>

<header class="site-header">
  <div class="brand">
    <div class="brand-square"></div>
    <span class="brand-name">zornival</span>
  </div>
  <nav class="main-nav">
    <a href="#" class="is-active">Home</a>
    <a href="#">About</a>
    <a href="#">Publisher</a>
    <a href="#">Advertiser</a>
    <a href="#">Contact</a>
    <a href="#" class="btn-consult">Request a Consult</a>
  </nav>
</header>

<section class="hero">
  <div class="hero-visual" role="img" aria-label="Mountaineers with backpacks and poles climbing a snowy mountain ridge under a blue sky"></div>
  <div class="hero-copy">
    <h1 class="hero-title">Welcome to zornival</h1>
    <p class="hero-text">zornival help websites to maximize their advertising revenues by optimizing their ad networks, configurations, technologies, etc.</p>
    <a href="#" class="btn-learn">Learn More</a>
  </div>
  <div class="hero-dots"><span class="is-active"></span><span></span><span></span><span></span></div>
</section>

<section class="intro">
  <h2 class="intro-title"><strong>One-stop shop</strong> for all your monetization needs</h2>
  <p class="intro-text">Let our team join your team to Optimize your adops and maximize your monetization Leave it to us to streamline, optimize, and manage your ad network relationships and operations. We'll take your revenues to the top.</p>
</section>

<section class="services">
  <div class="service service--left">
    <div class="service-icon"><svg viewBox="0 0 60 60"><rect x="8" y="38" width="7" height="14"/><rect x="20" y="32" width="7" height="20"/><rect x="32" y="26" width="7" height="26"/><rect x="44" y="20" width="7" height="32"/><path d="M8 30 L22 20 L32 24 L50 8"/><path d="M20 6 v14 M24 9 h-6 a3 3 0 0 0 0 5 h4 a3 3 0 0 1 0 5 h-6"/></svg></div>
    <span class="service-chevron">&gt;</span>
    <div class="service-body"><h3 class="service-title">Monetization Strategy &amp; Planning:</h3><p class="service-text">There's no "one size fits all" ads strategy. We help you find the winning combination, placements and mix for your adspace offer.</p></div>
  </div>

  <div class="service service--right">
    <div class="service-icon"><svg viewBox="0 0 60 60"><rect x="6" y="8" width="42" height="38" rx="3"/><path d="M6 16 h42 M12 24 h12 M12 31 h12 M12 38 h8"/><circle cx="44" cy="44" r="10"/><path d="M44 39 v10 M41 42 h5"/></svg></div>
    <span class="service-chevron">&lt;</span>
    <div class="service-body"><h3 class="service-title">Network Configurations:</h3><p class="service-text">From header bidders, to video, to native, to display, we create your optimum mix for maximum monetization: Screening, implementation, testing, measurement, and ongoing optimization to keep revenues at a max.</p></div>
  </div>

  <div class="service service--left">
    <div class="service-icon"><svg viewBox="0 0 60 60"><circle cx="22" cy="30" r="14"/><circle cx="38" cy="30" r="14"/></svg></div>
    <span class="service-chevron">&gt;</span>
    <div class="service-body"><h3 class="service-title">Access to Premium Brellix Vantrix Account:</h3><p class="service-text">Get the same rates as the big guys, with individualized, ongoing Vantrix optimization in our Brellix partner account, including access to our select premium marketplace deals.</p></div>
  </div>

  <div class="service service--right">
    <div class="service-icon"><svg viewBox="0 0 60 60"><path d="M4 24 L16 14 L26 18 L34 14 L56 24"/><path d="M14 34 L26 44 a3 3 0 0 0 4 -4 M22 38 l10 8 a3 3 0 0 0 4 -4 L26 32 M30 34 l8 6 a3 3 0 0 0 4 -4 L30 26 L24 30"/><path d="M4 24 L14 34 M56 24 L46 36"/></svg></div>
    <span class="service-chevron">&lt;</span>
    <div class="service-body"><h3 class="service-title">Contract Negotiation &amp; Relationship Management:</h3><p class="service-text">We help to make sure you are getting the best possible pricing and terms, and keep the relations to make sure the premium offers keep coming your way.</p></div>
  </div>

  <div class="service service--left">
    <div class="service-icon"><svg viewBox="0 0 60 60"><ellipse cx="24" cy="12" rx="16" ry="6"/><path d="M8 12 v30 a16 6 0 0 0 20 5 M40 12 v16 M8 22 a16 6 0 0 0 32 0 M8 32 a16 6 0 0 0 22 4"/><circle cx="44" cy="44" r="6"/><path d="M44 32 v4 M44 52 v4 M32 44 h4 M52 44 h4"/></svg></div>
    <span class="service-chevron">&gt;</span>
    <div class="service-body"><h3 class="service-title">Ad server set-up, training &amp; troubleshooting:</h3><p class="service-text">Header Bidding, Video, Native, Display...we stay on top of the technologies, so you don't have to.</p></div>
  </div>

  <div class="service service--right">
    <div class="service-icon"><svg viewBox="0 0 60 60"><path d="M4 48 h52"/><path d="M8 42 L20 34 L28 38 L40 24 L52 14"/><circle cx="40" cy="20" r="6"/><path d="M44 24 l6 6"/></svg></div>
    <span class="service-chevron">&lt;</span>
    <div class="service-body"><h3 class="service-title">Ad tag implementation &amp; tracking:</h3><p class="service-text">Let us take care of the details: orders, CPMs, scheduling, targeting, volumes, frequency caps.</p></div>
  </div>

  <div class="service service--left">
    <div class="service-icon"><svg viewBox="0 0 60 60"><rect x="6" y="38" width="7" height="14"/><rect x="17" y="32" width="7" height="20"/><rect x="28" y="26" width="7" height="26"/><rect x="39" y="20" width="7" height="32"/><path d="M50 52 V8 M44 14 L50 8 L56 14"/></svg></div>
    <span class="service-chevron">&gt;</span>
    <div class="service-body"><h3 class="service-title">Propriety Campaign Performance &amp; Reporting Tools:</h3><p class="service-text">Daily reporting, continuous monitoring for performance, discrepancies, and optimization.</p></div>
  </div>

  <div class="service service--right">
    <div class="service-icon"><svg viewBox="0 0 60 60"><rect x="6" y="10" width="48" height="40" rx="3"/><rect x="14" y="18" width="14" height="12"/><path d="M34 20 h12 M34 27 h12 M14 36 h32 M14 42 h32"/></svg></div>
    <span class="service-chevron">&lt;</span>
    <div class="service-body"><h3 class="service-title">Propriety Header Bidder Implementation:</h3><p class="service-text">Our "special sauce" header bidder will maximize fill and return.</p></div>
  </div>

  <div class="service service--left">
    <div class="service-icon"><svg viewBox="0 0 60 60"><circle cx="30" cy="16" r="10"/><path d="M30 10 v12 M24 16 h12"/><circle cx="16" cy="36" r="5"/><circle cx="30" cy="34" r="5"/><circle cx="44" cy="36" r="5"/><path d="M8 52 a8 8 0 0 1 16 0 M22 52 a8 8 0 0 1 16 0 M36 52 a8 8 0 0 1 16 0"/></svg></div>
    <span class="service-chevron">&gt;</span>
    <div class="service-body"><h3 class="service-title">Audience Segmentation, Targeting &amp; Marketing:</h3><p class="service-text">Target, segment, package &amp; sell your audiences to the right advertisers for maximum revenues.</p></div>
  </div>

  <div class="service service--right">
    <div class="service-icon"><svg viewBox="0 0 60 60"><circle cx="24" cy="24" r="8"/><path d="M24 8 v6 M24 34 v6 M8 24 h6 M34 24 h6 M13 13 l4 4 M31 31 l4 4 M13 35 l4 -4 M31 17 l4 -4"/><circle cx="44" cy="44" r="5"/><path d="M44 34 v4 M44 50 v4 M34 44 h4 M50 44 h4"/></svg></div>
    <span class="service-chevron">&lt;</span>
    <div class="service-body"><h3 class="service-title">Ongoing Optimization:</h3><p class="service-text">The Holy Grail. We never stop tweaking and tightening to keep your revenues optimized and adjusted for seasonal fluctuations.</p></div>
  </div>

  <div class="service service--left">
    <div class="service-icon"><svg viewBox="0 0 60 60"><rect x="8" y="6" width="44" height="48" rx="3"/><path d="M16 18 l3 3 l5 -6 M16 30 l3 3 l5 -6 M16 42 l3 3 l5 -6 M30 19 h14 M30 31 h14 M30 43 h14"/></svg></div>
    <span class="service-chevron">&gt;</span>
    <div class="service-body"><h3 class="service-title">Quality Control:</h3><p class="service-text">We work with you to keep bad ads out, and block lists up-to-date.</p></div>
  </div>

  <div class="service service--right">
    <div class="service-icon"><svg viewBox="0 0 60 60"><path d="M14 6 v48 M30 6 v48 M46 6 v48"/><rect x="9" y="30" width="10" height="8" rx="2"/><rect x="25" y="14" width="10" height="8" rx="2"/><rect x="41" y="38" width="10" height="8" rx="2"/></svg></div>
    <span class="service-chevron">&lt;</span>
    <div class="service-body"><h3 class="service-title">Direct Advertiser Management:</h3><p class="service-text">We field &amp; manage your direct advertiser enquiries and campaigns.</p></div>
  </div>

  <div class="service service--left">
    <div class="service-icon"><svg viewBox="0 0 60 60"><path d="M22 40 a14 14 0 1 1 16 0 v6 h-16 z"/><path d="M23 50 h14 M25 54 h10 M30 40 v-10 l-4 -4 M30 30 l4 -4"/></svg></div>
    <span class="service-chevron">&gt;</span>
    <div class="service-body"><h3 class="service-title">Business Development:</h3><p class="service-text">We stay on top of the latest trends and best technologies, so you don't have to!</p></div>
  </div>
</section>

<section class="subscribe">
  <h2 class="subscribe-title">Subscribe to our mailing list</h2>
  <div class="subscribe-field">Name</div>
  <div class="subscribe-field">Email</div>
  <div class="subscribe-btn">SUBSCRIBE</div>
</section>

<footer class="site-footer">
  <div class="footer-col quick-links">
    <h4 class="footer-heading">Quick Links</h4>
    <ul>
      <li>Home</li><li>About</li><li>Publisher</li><li>Advertiser</li><li>Contact</li><li>Request a Consult</li>
    </ul>
  </div>
  <div class="footer-col contact">
    <h4 class="footer-heading">Contact Us</h4>
    <div class="contact-item"><svg viewBox="0 0 16 16"><path d="M8 0 a5.5 5.5 0 0 1 5.5 5.5 c0 4 -5.5 10.5 -5.5 10.5 S2.5 9.5 2.5 5.5 A5.5 5.5 0 0 1 8 0 z M8 3.5 a2 2 0 1 0 0.01 0 z"/></svg><span>48 Harlow Crest Dr<br>Marvale Bay, CA 90417</span></div>
    <div class="contact-item"><svg viewBox="0 0 16 16"><path d="M3 1 l3 0 l1.5 4 l-2 1.5 a9 9 0 0 0 4 4 l1.5 -2 l4 1.5 l0 3 a2 2 0 0 1 -2 2 A13 13 0 0 1 1 3 a2 2 0 0 1 2 -2 z"/></svg><span>555.014.7720</span></div>
    <div class="contact-item"><svg viewBox="0 0 16 16"><path d="M1 3 h14 v10 h-14 z M1 3 l7 6 l7 -6" fill="none" stroke="#fff" stroke-width="1.5"/></svg><span>info@zornival.com</span></div>
  </div>
  <div class="footer-col message">
    <h4 class="footer-heading">Send a Message</h4>
    <div class="message-field">Name</div>
    <div class="message-field">Email</div>
    <div class="message-field message-field--area">Message</div>
    <div class="message-btn">SUBMIT</div>
  </div>
  <div class="footer-brand">
    <div class="brand-square"></div>
    <span class="brand-name">zornival</span>
  </div>
</footer>

<div class="copyright">
  <span>COPYRIGHT © 2016 ZORNIVAL. ALL RIGHTS RESERVED.</span>
  <div class="social"><span></span><span></span><span></span></div>
</div>

</body>
</html>
```